Basket Lane Inc.
Title of service: "Wardrobe Van" - mobile scrub uniform store, where we go to nursing homes and employees buy their uniforms through us

Photos to consider: nurses, aides, people who work in nursing homes.

need a postcard design for direct mailing nursing homes to promote our traveling nursing uniform store to nursing homes
Contact details:
Phone 18004729316

Points of Interest to Mention on Card:
Family-Owned Business, Providing impeccable service since 1975
Large Inventory
Stock includes Marlowe, Pellham Brands, budget brands
Reduced Prices
Will work with your schedule to fit your needs
Designated stock colors for your department staff
Special order items are available
150+ top choices per size (XXS-5XL)

Target Market(s)

Director of nursing, nursing homes staff

Industry/Entity Type

Store

```html
<!DOCTYPE html>
<html lang="en">
<head>
<meta charset="utf-8">
<title>Wardrobe Van – Postcard</title>
<link rel="stylesheet" href="https://fonts.googleapis.com/css2?family=Anton&family=Lato:wght@400;700&family=Roboto+Condensed:wght@700&family=Libre+Baskerville&display=swap">
<style>
  :root {
    --page: #e9eaec;
    --white: #ffffff;
    --sky-light: #d3ecf8;
    --sky: #8fcdee;
    --sky-deep: #3fa3dc;
    --brand-blue: #2f97d6;
    --navy: #144a86;
    --lime: #b8d452;
    --green: #8db43a;
    --green-dark: #6c8f27;
    --ink: #1b1b1b;
    --rule: #333333;
  }
  * { box-sizing: border-box; margin: 0; padding: 0; }
  html, body { width: 900px; height: 1200px; overflow: hidden; }
  body { background: var(--page); position: relative; font-family: "Lato", sans-serif; color: var(--ink); }

  .card { position: absolute; background: var(--white); box-shadow: 0 4px 14px rgba(0,0,0,.18); overflow: hidden; }

  /* Front */
  .card-front { left: 120px; top: 57px; width: 647px; height: 500px; }
  .card-front .art { position: absolute; inset: 0; }
  .brand-title {
    position: absolute; left: 58px; top: 42px;
    font-family: "Anton", sans-serif; font-size: 76px; line-height: 86px;
    color: var(--brand-blue); letter-spacing: 1px;
  }
  .call-bar {
    position: absolute; left: 88px; top: 260px; width: 230px; height: 43px;
    background: linear-gradient(90deg, var(--green-dark), var(--green) 40%, var(--lime));
    display: flex; align-items: center; justify-content: center; gap: 6px;
    color: var(--white); font-family: "Roboto Condensed", sans-serif;
  }
  .call-bar .label { font-size: 17px; }
  .call-bar .number { font-size: 23px; color: #1e2a10; }
  .intro-box {
    position: absolute; left: 21px; top: 331px; width: 269px; height: 107px;
    background: linear-gradient(90deg, var(--green), var(--lime));
    padding: 14px 15px; font-size: 15px; line-height: 19.5px; color: #1c2410;
  }

  /* Back */
  .card-back { left: 118px; top: 607px; width: 670px; height: 520px; }
  .back-panel {
    position: absolute; left: 23px; top: 21px; width: 390px; height: 475px;
    background: linear-gradient(180deg, var(--sky) 0%, var(--sky-light) 25%, var(--sky-light) 45%, var(--sky) 75%, var(--sky-deep) 100%);
  }
  .band {
    position: absolute; left: 15px; width: 408px;
    background: linear-gradient(90deg, var(--green-dark), var(--lime) 35%, var(--lime) 65%, var(--green-dark));
    box-shadow: 0 3px 6px rgba(0,0,0,.25);
  }
  .band-heritage { top: 51px; height: 87px; text-align: center; padding-top: 16px; }
  .band-heritage .tagline { font-weight: 700; font-size: 13.5px; color: var(--ink); }
  .band-heritage .since { font-family: "Roboto Condensed", sans-serif; font-size: 35px; line-height: 42px; color: var(--navy); }
  .about-tag {
    position: absolute; left: 0; top: 163px; width: 418px; height: 34px;
  }
  .about-tag span {
    position: absolute; left: 0; right: 0; top: 5px; text-align: center;
    font-family: "Libre Baskerville", serif; font-size: 20px; color: var(--ink);
  }
  .about-copy {
    position: absolute; left: 53px; width: 346px; font-size: 15px; line-height: 18.5px; color: var(--ink);
  }
  .about-copy.first { top: 208px; text-align: justify; text-align-last: justify; }
  .about-copy.second { top: 303px; }
  .about-rule { position: absolute; left: 53px; top: 293px; width: 340px; border-top: 2px solid var(--rule); }
  .band-contact { top: 380px; height: 85px; padding: 10px 0 0 35px; }
  .contact-row { display: flex; align-items: center; gap: 12px; font-weight: 700; font-size: 15.5px; height: 24px; color: var(--ink); }
  .contact-row svg { width: 14px; height: 14px; flex: none; }
  .band-contact .mark {
    position: absolute; right: 30px; top: 14px; width: 98px; text-align: center;
    font-family: "Anton", sans-serif; font-size: 26px; line-height: 28px; color: rgba(120,150,110,.55);
  }
  .stamp-box { position: absolute; left: 575px; top: 93px; width: 62px; height: 67px; border: 1px solid #666; }
  .address-line { position: absolute; left: 454px; width: 183px; border-top: 1px solid #444; }
</style>
</head>
<body>

<section class="card card-front">
  <svg class="art" width="647" height="500" viewBox="0 0 647 500">
    <defs>
      <linearGradient id="frontBlue" x1="0" y1="0" x2="0.3" y2="1">
        <stop offset="0" stop-color="#a9daf3"/>
        <stop offset="0.55" stop-color="#69bbe8"/>
        <stop offset="1" stop-color="#3fa3dc"/>
      </linearGradient>
      <linearGradient id="photoTone" x1="0" y1="0" x2="1" y2="1">
        <stop offset="0" stop-color="#ffffff"/>
        <stop offset="0.6" stop-color="#eef2f5"/>
        <stop offset="1" stop-color="#b9d5ea"/>
      </linearGradient>
    </defs>
    <rect width="647" height="500" fill="url(#frontBlue)"/>
    <polygon points="428,0 647,0 647,500 225,500" fill="url(#photoTone)" role="img" aria-label="Photo of smiling nursing home staff in white coats and scrubs giving a thumbs up"/>
    <polygon points="425,0 432,0 229,500 222,500" fill="#b8d452"/>
  </svg>
  <h1 class="brand-title">WARDROBE<br>VAN</h1>
  <div class="call-bar"><span class="label">CALL US :</span><span class="number">18004729316</span></div>
  <p class="intro-box">Mobile scrub uniform store, where we go to nursing homes and employees buy their uniforms through us</p>
</section>

<section class="card card-back">
  <div class="back-panel"></div>

  <div class="band band-heritage">
    <p class="tagline">Family-Owned Business, Providing impeccable service</p>
    <p class="since">since 1975</p>
  </div>

  <div class="about-tag">
    <svg width="418" height="34" viewBox="0 0 418 34">
      <line x1="40" y1="17" x2="378" y2="17" stroke="#8db43a" stroke-width="1"/>
      <polygon points="150,0 268,0 282,17 268,34 150,34 136,17" fill="#b8d452"/>
    </svg>
    <span>ABOUT US</span>
  </div>

  <p class="about-copy first">Large Inventory Stock includes Marlowe, Pellham Brands, budget brands. Will work with your schedule to fit your needs Designated stock colors for your department staff Special</p>
  <div class="about-rule"></div>
  <p class="about-copy second">order items are available<br>150+ top choices per size (XXS-5XL).</p>

  <div class="band band-contact">
    <div class="contact-row">
      <svg viewBox="0 0 24 24"><path fill="#144a86" d="M6.6 10.8a15 15 0 0 0 6.6 6.6l2.2-2.2a1 1 0 0 1 1-.25 11.4 11.4 0 0 0 3.6.57 1 1 0 0 1 1 1V20a1 1 0 0 1-1 1A17 17 0 0 1 3 4a1 1 0 0 1 1-1h3.5a1 1 0 0 1 1 1c0 1.25.2 2.45.57 3.57a1 1 0 0 1-.25 1z"/></svg>
      <span>18004729316</span>
    </div>
    <div class="contact-row">
      <svg viewBox="0 0 24 24"><path fill="#144a86" d="M12 3 2 12h3v8h5v-6h4v6h5v-8h3z"/></svg>
      <span>your address</span>
    </div>
    <div class="contact-row">
      <svg viewBox="0 0 24 24"><path fill="#144a86" d="M2 5h20v14H2z"/><path fill="none" stroke="#b8d452" stroke-width="1.8" d="M2 5l10 8 10-8"/></svg>
      <span>your email address</span>
    </div>
    <p class="mark">WARDROBE<br>VAN</p>
  </div>

  <div class="stamp-box"></div>
  <div class="address-line" style="top:259px"></div>
  <div class="address-line" style="top:290px"></div>
  <div class="address-line" style="top:321px"></div>
</section>

</body>
</html>
```